Website for Kitchen Showroom

We need a website for our Kitchen Showroom. Will be 10 pages in total. Example of a website we like can be found at http://www.velmarabo.co.uk/ with the image on the front page being a java script slideshow picking up images from a directory that I can update. Looking for simple SEO
I have the wording/ sitemap/ images all ready to go and I am looking for a quick turn around.
Thank you for your time. Rob

```html
<!DOCTYPE html>
<html lang="en">
<head>
<meta charset="utf-8">
<title>Brightwood – Designer Kitchens</title>
<link rel="stylesheet" href="https://fonts.googleapis.com/css2?family=Arimo:wght@400;700&display=swap">
<style>
  :root {
    --page-top: #1c1c1c;
    --page-bottom: #2c2c2c;
    --panel: #000000;
    --green: #6cc24a;
    --green-dark: #1f8a3a;
    --text: #ffffff;
    --muted: #b9b9b9;
    --footer-text: #9a9a9a;
    --box-line: #3a3a3a;
  }
  * { box-sizing: border-box; margin: 0; padding: 0; }
  html, body { width: 1200px; height: 793px; overflow: hidden; }
  body {
    position: relative;
    background: linear-gradient(var(--page-top), var(--page-bottom));
    font-family: "Arimo", Arial, sans-serif;
    color: var(--text);
  }
  .brand {
    position: absolute; left: 39px; top: 58px;
    display: flex; align-items: center; gap: 14px;
  }
  .brand-mark { width: 56px; height: 56px; background: var(--green); }
  .brand-name { font-size: 40px; line-height: 56px; font-weight: 400; color: var(--muted); }
  .brand-rule {
    position: absolute; left: 39px; top: 128px; width: 468px; height: 2px;
    background: linear-gradient(90deg, #777, #999 60%, #555);
  }
  .nav-item {
    position: absolute; height: 30px;
    border: 1px solid var(--box-line); background: #0d0d0d;
    color: var(--text); font-size: 14px; text-align: center; line-height: 30px;
    text-decoration: none;
  }
  .nav-item.top { height: 40px; line-height: 30px; }
  .nav-item.top::after {
    content: ""; position: absolute; left: 0; right: 0; bottom: 0; height: 9px;
    background: linear-gradient(90deg, var(--green-dark), var(--green));
  }
  .nav-item.top.grey::after { background: linear-gradient(90deg, #666, #fff 50%, #888); }
  .nav-item.active { color: var(--green); }
  .nav-divider { position: absolute; top: 80px; width: 2px; height: 96px; background: var(--green); }
  .submenu-item {
    position: absolute; left: 1002px; width: 159px; height: 27px; z-index: 2;
    border: 1px solid var(--box-line); background: #0d0d0d;
    font-size: 14px; line-height: 26px; padding-left: 6px; color: var(--text);
    white-space: nowrap;
  }
  .cursor { position: absolute; left: 1128px; top: 145px; z-index: 3; }
  .content {
    position: absolute; left: 39px; top: 226px; width: 1122px; height: 497px;
    background: var(--panel);
  }
  .welcome { position: absolute; left: 67px; top: 268px; width: 420px; }
  .welcome-title { font-size: 47px; font-weight: 700; color: var(--green); line-height: 48px; }
  .welcome-sub { font-size: 24px; font-weight: 700; color: var(--green); line-height: 30px; }
  .intro { position: absolute; left: 67px; top: 367px; width: 410px; font-size: 13.5px; line-height: 15.5px; }
  .intro p { margin-bottom: 15px; }
  .intro .name-lead { font-size: 21px; line-height: 22px; white-space: nowrap; }
  .intro a { color: var(--green); text-decoration: none; }
  .feature-title {
    position: absolute; left: 517px; top: 306px; font-size: 34px; color: var(--muted);
    font-weight: 400; white-space: nowrap;
  }
  .feature-vrule { position: absolute; left: 508px; top: 301px; width: 1px; height: 370px; background: var(--green); }
  .feature-hrule { position: absolute; left: 483px; top: 359px; width: 650px; height: 1px; background: var(--green); }
  .feature-photo {
    position: absolute; left: 519px; top: 370px; width: 614px; height: 299px;
    background: linear-gradient(100deg, #d9d9d9 0%, #6a6a6a 30%, #1a1a1a 55%, #8a8a8a 80%, #cfcfcf 100%);
  }
  .footer {
    position: absolute; left: 39px; top: 739px; width: 1122px; height: 52px;
    background: var(--panel); color: var(--footer-text); font-size: 14px;
  }
  .footer-accent { position: absolute; left: 0; top: 0; width: 9px; height: 52px; background: var(--green); }
  .footer-copy { position: absolute; left: 28px; top: 17px; }
  .footer-links { position: absolute; left: 874px; top: 17px; }
</style>
</head>
<body>
  <main>
    <div class="content"></div>
    <section class="welcome">
      <h1 class="welcome-title">Welcome to</h1>
      <h2 class="welcome-sub">Brightwood.</h2>
    </section>
    <section class="intro">
      <p>The region's exclusive kitchen manufacturer based in Larkfield. If you are seeking the highest quality kitchen, yet at a price that is a little more affordable, Brightwood is the company you've been searching for.</p>
      <p><span class="name-lead">Brightwood</span> showroom is located less than 25 kilometers from the city centre, so easy to get to with easy access from the Northgate Highway.</p>
      <p>On this site, you can view some of our designer kitchens, read <a href="#">testimonials</a> from our clients or just browse through our site to find out more. We hope you will find our site inspiring and put <span class="name-lead">Brightwood</span> at the top of your list of kitchen showrooms you simply must visit.</p>
      <p>Pop into our showroom. We can chat about your plans and ideas for your new kitchen and maybe we can give you a few ideas of our own. Or <a href="#">contact us</a> to arrange a no obligation consultation with one of our kitchen designers and if required we will bring the showroom to you.</p>
    </section>

    <h2 class="feature-title">Designer Kitchens by Brightwood</h2>
    <span class="feature-vrule"></span>
    <span class="feature-hrule"></span>
    <div class="feature-photo" role="img" aria-label="Black and white photo of a dining room with a glass table and tall black chairs"></div>
  </main>

  <header>
    <div class="brand">
      <span class="brand-mark"></span>
      <span class="brand-name">Brightwood</span>
    </div>
    <div class="brand-rule"></div>

    <nav>
      <a class="nav-item top" style="left:510px;top:90px;width:160px">Quality Page</a>
      <a class="nav-item top" style="left:674px;top:90px;width:160px">Order Page</a>
      <a class="nav-item top" style="left:838px;top:90px;width:158px">Kitchen Designers</a>
      <a class="nav-item top grey" style="left:1000px;top:90px;width:161px">Kitchen Instalation</a>

      <a class="nav-item" style="left:348px;top:135px;width:159px">Home Page</a>
      <a class="nav-item" style="left:510px;top:135px;width:160px">Design Consultation</a>
      <a class="nav-item" style="left:674px;top:135px;width:160px">Contact Us</a>
      <a class="nav-item" style="left:838px;top:135px;width:158px">Design</a>
      <a class="nav-item active" style="left:1000px;top:135px;width:161px">Links Page</a>

      <span class="nav-divider" style="left:670px"></span>
      <span class="nav-divider" style="left:834px"></span>
      <span class="nav-divider" style="left:997px"></span>

      <div class="submenu-item" style="top:168px">Laminates &amp; Benchtops</div>
      <div class="submenu-item" style="top:199px">Engineered Stones</div>
      <div class="submenu-item" style="top:230px">Granite and Marble</div>
      <div class="submenu-item" style="top:260px">Splashbacks</div>
    </nav>
    <svg class="cursor" width="16" height="24" viewBox="0 0 16 24" aria-hidden="true">
      <path d="M1 1 L1 19 L5 15 L8 22 L11 21 L8 14 L14 14 Z" fill="#111" stroke="#ddd" stroke-width="1.2"/>
    </svg>
  </header>

  <footer class="footer">
    <span class="footer-accent"></span>
    <span class="footer-copy">Copyright ©2011. All right reserved.</span>
    <span class="footer-links">Privacy Policy / Terms of use</span>
  </footer>
</body>
</html>
```